PowerPoint template for my training workshop business

I would like to have a PowerPoint template created using my logo and palette materials created by Brivantelox. I train and facilitate workshops using PowerPoint in both corporate and public settings.

I have attached the original design elements to this request.

```html
<!DOCTYPE html>
<html lang="en">
<head>
<meta charset="utf-8">
<title>Workshop Slide Template</title>
<link href="https://fonts.googleapis.com/css2?family=Mulish:wght@300;400;700;800;900&display=swap" rel="stylesheet">
<style>
  :root {
    --orange: #ffab00;
    --orange-light: #ffc93c;
    --charcoal: #2b2b2b;
    --footer: #4b4b4b;
    --paper: #fcf9f5;
    --ink: #262626;
    --muted: #8c8c8c;
    --white: #ffffff;
  }
  html, body {
    margin: 0;
    padding: 0;
    overflow: hidden;
    background: var(--paper);
  }
  .slide {
    position: relative;
    width: 1200px;
    height: 676px;
    overflow: hidden;
    background: var(--paper);
    font-family: "Mulish", sans-serif;
  }
  .header {
    position: absolute;
    left: 0; top: 0;
    width: 1200px; height: 91px;
  }
  .header svg { position: absolute; left: 0; top: 0; }
  .project-title {
    position: absolute;
    left: 26px; top: 22px;
    margin: 0;
    font-size: 39px;
    font-weight: 900;
    color: var(--ink);
    letter-spacing: 0.2px;
  }
  .brand {
    position: absolute;
    left: 922px; top: 18px;
    display: flex;
    align-items: center;
    gap: 10px;
  }
  .brand-dot {
    width: 40px; height: 40px;
    border-radius: 50%;
    background: var(--orange);
    flex: none;
  }
  .brand-name {
    font-weight: 800;
    font-size: 17px;
    line-height: 21px;
    color: var(--orange);
    text-transform: uppercase;
    letter-spacing: 1px;
  }
  .side-accent {
    position: absolute;
    left: 0; top: 212px;
    width: 33px; height: 274px;
    background: var(--orange);
  }
  .article {
    position: absolute;
    left: 65px; top: 146px;
    width: 580px;
  }
  .article h2 {
    margin: 0 0 2px;
    font-size: 30px;
    font-weight: 800;
    color: var(--ink);
  }
  .article p {
    margin: 0;
    font-size: 17.6px;
    font-weight: 400;
    line-height: 30px;
    color: var(--muted);
  }
  .article p + p { margin-top: 30px; }
  .article p.tight { margin-top: 0; }
  .photo {
    position: absolute;
    left: 668px; top: 133px;
    width: 472px; height: 393px;
    background: linear-gradient(135deg, #c9d3cc 0%, #ece7e0 45%, #d9c2ae 70%, #efe6dc 100%);
  }
  .caption {
    position: absolute;
    left: 668px; top: 528px;
    width: 472px; height: 84px;
    display: flex;
  }
  .caption-title {
    flex: 1;
    background: var(--orange);
    display: flex;
    align-items: center;
    justify-content: center;
    font-size: 30px;
    font-weight: 800;
    color: var(--ink);
  }
  .caption-arrow {
    width: 92px;
    background: var(--charcoal);
    display: flex;
    align-items: center;
    justify-content: center;
  }
  .footer {
    position: absolute;
    left: 0; top: 646px;
    width: 1200px; height: 30px;
    background: var(--footer);
  }
  .copyright {
    position: absolute;
    left: 6px; top: 8px;
    font-size: 14px;
    font-weight: 700;
    color: var(--white);
  }
  .page-number {
    position: absolute;
    left: 1133px; top: 614px;
    width: 50px; height: 50px;
    border-radius: 50%;
    border: 3px solid var(--white);
    background: var(--orange);
    color: var(--white);
    font-size: 17px;
    font-weight: 800;
    display: flex;
    align-items: center;
    justify-content: center;
  }
</style>
</head>
<body>
<div class="slide">
  <header class="header">
    <svg width="1200" height="91" viewBox="0 0 1200 91">
      <defs>
        <linearGradient id="band" x1="0" y1="1" x2="0" y2="0">
          <stop offset="0" stop-color="#ffa900"/>
          <stop offset="1" stop-color="#ffc93c"/>
        </linearGradient>
      </defs>
      <rect width="1200" height="91" fill="var(--charcoal)"/>
      <path d="M0 0 H868 C885 20 900 70 925 91 H0 Z" fill="url(#band)"/>
      <path d="M872 0 C890 22 904 70 932 91" fill="none" stroke="#ffffff" stroke-width="3"/>
    </svg>
    <h1 class="project-title">PROJECT TITLE HERE</h1>
    <div class="brand">
      <span class="brand-dot"></span>
      <span class="brand-name">Marisol Venner<br>Coaching</span>
    </div>
  </header>

  <div class="side-accent"></div>

  <section class="article">
    <h2>Image Title here</h2>
    <p>Do you have a business presentation PowerPoint to give this week? Is the deadline for your pitch approaching fast? Or, is the clock tick-ing down to the date of your speaking engagement?</p>
    <p>Do you have a business presentation PowerPoint to give this week? Is the deadline for your pitch approaching fast? Or, is the clock tick-ing down to the date of your speaking engagement?</p>
    <p>If so, your needs are immediate. It's critical that you create a profes-sional presentation that's designed for business results.</p>
    <p class="tight">Do you have a business presentation PowerPoint to give this week? Is the deadline for your pitch approaching fast? Or, is the clock tick-ing down to the date of your speaking engagement?</p>
  </section>

  <div class="photo" role="img" aria-label="Photo of a woman taking notes at a desk beside a laptop"></div>
  <div class="caption">
    <div class="caption-title">Image Title here</div>
    <div class="caption-arrow">
      <svg width="16" height="20" viewBox="0 0 16 20">
        <path d="M4 3 L12 10 L4 17" fill="none" stroke="#ffffff" stroke-width="2.6" stroke-linecap="round" stroke-linejoin="round"/>
      </svg>
    </div>
  </div>

  <footer class="footer">
    <span class="copyright">Copyright text here</span>
  </footer>
  <div class="page-number">01</div>
</div>
</body>
</html>
```